Billboard design for retail kitchen cabinet business

We have a large 7,000 square-foot showroom of beautiful kitchen cabinet displays of all different designs and price ranges. In business for over 50 years with expert designers.
Full size Halvard Media 14' X 48' billboard
Target Market(s)
Retail public on high traffic Los Angeles streets

```html
<!DOCTYPE html>
<html lang="en">
<head>
<meta charset="utf-8">
<title>The Cabinet Loft – Billboard</title>
<link rel="stylesheet" href="https://fonts.googleapis.com/css2?family=Oswald:wght@400;500;700&family=Montserrat:wght@400;500&display=swap">
<style>
  :root {
    --amber: #f2a50c;
    --ink: #2b2b2b;
    --rule: #555555;
    --white: #ffffff;
    --backdrop: #e9eaec;
  }
  * { margin: 0; padding: 0; box-sizing: border-box; }
  html, body { width: 1200px; height: 1200px; overflow: hidden; }
  body { background: var(--backdrop); position: relative; font-family: "Oswald", sans-serif; }

  .billboard {
    position: absolute; left: 30px; top: 433px;
    width: 1140px; height: 334px;
    background: var(--white);
    box-shadow: 0 6px 24px rgba(0,0,0,.18);
  }
  .billboard__frame { position: absolute; inset: 0; }

  .brand {
    position: absolute; left: 34px; top: 56px;
    display: flex; align-items: center; gap: 12px;
  }
  .brand__mark { width: 22px; height: 22px; background: var(--ink); }
  .brand__name {
    font-family: "Oswald", sans-serif; font-weight: 700;
    font-size: 36px; line-height: 1; color: var(--ink); letter-spacing: .5px;
    white-space: nowrap;
  }
  .brand__tagline {
    position: absolute; left: 170px; top: 112px;
    font-family: "Montserrat", sans-serif; font-size: 12px; font-weight: 500;
    letter-spacing: 2.4px; line-height: 1.45; color: var(--ink);
  }

  .pillars {
    position: absolute; left: 20px; top: 200px; height: 46px;
    display: flex; align-items: center;
    font-family: "Oswald", sans-serif; font-weight: 500;
    font-size: 22px; color: var(--ink);
    letter-spacing: -.2px; white-space: nowrap;
  }
  .pillars__dot {
    display: inline-block; width: 5px; height: 5px; background: var(--ink);
    margin: 0 6px;
  }

  .phones {
    position: absolute; left: 22px; top: 249px;
    font-family: "Oswald", sans-serif; font-weight: 500;
    font-size: 27px; line-height: 34px; color: var(--ink); letter-spacing: -.4px;
    white-space: nowrap;
  }
  .range-note {
    position: absolute; left: 22px; top: 289px; width: 310px;
    font-family: "Oswald", sans-serif; font-weight: 400;
    font-size: 14px; line-height: 16px; color: var(--ink);
    text-align: center; text-transform: uppercase;
  }

  .contact {
    position: absolute; left: 360px; top: 276px; width: 772px; height: 48px;
    display: flex; align-items: center; justify-content: space-between;
    padding: 0 14px 0 18px;
    font-family: "Montserrat", sans-serif; font-size: 24px; color: var(--ink);
  }
  .contact__item { display: flex; align-items: center; gap: 8px; white-space: nowrap; }
  .contact__icon { width: 20px; height: 20px; }
</style>
</head>
<body>
  <section class="billboard">
    <svg class="billboard__frame" viewBox="0 0 1140 334" width="1140" height="334">
      <defs>
        <linearGradient id="kitchen-tones" x1="0" y1="0" x2="1" y2="0">
          <stop offset="0" stop-color="#d8cbb4"/>
          <stop offset=".45" stop-color="#c9a27a"/>
          <stop offset=".7" stop-color="#9a5a32"/>
          <stop offset="1" stop-color="#6b3a1f"/>
        </linearGradient>
      </defs>
      <polygon points="8,8 410,8 350,326 8,326" fill="#fff" stroke="#f2a50c" stroke-width="2.5"/>
      <polygon points="8,200 374,200 365,246 8,246" fill="#f2a50c"/>
      <line x1="22" y1="286" x2="336" y2="286" stroke="#555" stroke-width="1"/>
      <polygon points="420,8 1132,8 1132,274 370,274" fill="url(#kitchen-tones)" stroke="#f2a50c" stroke-width="2.5"
               role="img" aria-label="Photo of a modern kitchen with white lacquer cabinets, walnut tall cabinets, island and pendant lights"/>
      <polygon points="370,274 1132,274 1132,326 360,326" fill="#f2a50c"/>
    </svg>

    <div class="brand">
      <span class="brand__mark"></span>
      <span class="brand__name">THE CABINET LOFT</span>
    </div>
    <p class="brand__tagline">BEAUTIFYING<br>KITCHENS SINCE 1965</p>

    <p class="pillars">QUALITY<span class="pillars__dot"></span>VALUE<span class="pillars__dot"></span>SERVICE<span class="pillars__dot"></span>SELECTION</p>
    <p class="phones">310.555.0142 | 800.555.0199</p>
    <p class="range-note">From traditional designs to<br>latest looks &amp; styles</p>

    <div class="contact">
      <span class="contact__item">
        <svg class="contact__icon" viewBox="0 0 20 20" fill="none" stroke="#2b2b2b" stroke-width="1.8">
          <rect x="2" y="5" width="16" height="11"/><polyline points="2,5 10,11 18,5"/>
        </svg>
        Info@TheCabinetLoft.net
      </span>
      <span class="contact__item">
        <svg class="contact__icon" viewBox="0 0 20 20" fill="none" stroke="#2b2b2b" stroke-width="1.6">
          <circle cx="10" cy="10" r="8"/><ellipse cx="10" cy="10" rx="3.5" ry="8"/>
          <line x1="2" y1="10" x2="18" y2="10"/><line x1="3.5" y1="5.5" x2="16.5" y2="5.5"/><line x1="3.5" y1="14.5" x2="16.5" y2="14.5"/>
        </svg>
        www.TheCabinetLoft.net
      </span>
    </div>
  </section>
</body>
</html>
```